Vardena General Painting Ltd. - Construction painting company providing high-quality service

We need a logo and business card design for a painting company that provides high-quality work for major developers and builders in Calgary, Alberta. Our projects include commercial high-rise residential towers. We would like designs that communicate professionalism and high quality service.
Updates
Need extra days to review
Target Market(s)
Developers and builders
Industry/Entity Type
Construction
Contact Information for Business Card
Company name, employee name, title, phone number, email address
Font styles to use
Colors
Designer to choose colors to be used in the design.
Look and feel
Each slider illustrates characteristics of the customer's brand and the style your logo design should communicate.

```html
<!DOCTYPE html>
<html lang="en">
<head>
<meta charset="utf-8">
<title>Vardena General Painting Ltd. – Business Card</title>
<link rel="stylesheet" href="https://fonts.googleapis.com/css2?family=Tinos:wght@400&family=PT+Sans:wght@400&display=swap">
<style>
  :root {
    --backdrop: #2b2b2b;
    --card: #1d1d1d;
    --silver: #bdbdbd;
    --silver-soft: #a9a9a9;
    --flame: #d6452a;
    --amber: #d9922c;
    --serif: "Tinos", "Times New Roman", serif;
    --sans: "PT Sans", Arial, sans-serif;
  }
  * { box-sizing: border-box; margin: 0; padding: 0; }
  html, body {
    width: 1200px; height: 600px; overflow: hidden;
    background: var(--backdrop);
  }
  .canvas {
    position: relative; width: 1200px; height: 600px;
  }
  .card {
    position: absolute; top: 164px;
    width: 466px; height: 272px;
    background: var(--card);
    border-radius: 16px;
    overflow: hidden;
  }
  .card--front { left: 123px; }
  .card--back  { left: 612px; }

  /* Front card */
  .brand-small {
    position: absolute; left: 42px; top: 118px;
    display: flex; align-items: center; gap: 8px;
  }
  .brand-mark {
    flex: none; width: 14px; height: 14px; background: var(--amber);
  }
  .brand-name {
    font-family: var(--serif); color: var(--silver);
    font-size: 15px; line-height: 1.1; letter-spacing: 0.5px;
    text-transform: uppercase; width: 160px;
  }
  .divider {
    position: absolute; left: 233px; top: 76px;
    width: 2px; height: 114px;
    background: linear-gradient(var(--amber), var(--flame));
  }
  .person {
    position: absolute; left: 252px; top: 98px;
  }
  .person-name {
    font-family: var(--serif); color: var(--silver);
    font-size: 22px; letter-spacing: 0.3px; line-height: 1.1;
  }
  .person-title {
    font-family: var(--sans); color: var(--flame);
    font-size: 13px; margin-top: 4px; letter-spacing: 0.3px;
  }
  .contact-list { list-style: none; margin-top: 10px; }
  .contact-item {
    display: flex; align-items: center; gap: 7px;
    font-family: var(--sans); color: var(--silver-soft);
    font-size: 12px; margin-top: 9px;
  }
  .contact-item svg { width: 11px; height: 11px; fill: var(--flame); }

  /* Back card */
  .brand-square {
    position: absolute; left: 52px; top: 76px;
    width: 120px; height: 120px;
    background: var(--amber);
  }
  .brand-large {
    position: absolute; left: 206px; top: 92px; width: 240px;
    font-family: var(--serif); color: var(--silver);
    font-size: 25px; line-height: 1.2; letter-spacing: 1.5px;
    text-transform: uppercase; text-align: center;
  }
</style>
</head>
<body>
<main class="canvas">
  <section class="card card--front">
    <div class="brand-small">
      <span class="brand-mark"></span>
      <span class="brand-name">Vardena General Painting Ltd.</span>
    </div>
    <div class="divider"></div>
    <div class="person">
      <p class="person-name">YOUR NAME</p>
      <p class="person-title">JOB TITLE</p>
      <ul class="contact-list">
        <li class="contact-item">
          <svg viewBox="0 0 24 24" aria-hidden="true"><path d="M6.6 10.8a15.1 15.1 0 0 0 6.6 6.6l2.2-2.2a1 1 0 0 1 1-.25 11.4 11.4 0 0 0 3.6.57 1 1 0 0 1 1 1V20a1 1 0 0 1-1 1A17 17 0 0 1 3 4a1 1 0 0 1 1-1h3.5a1 1 0 0 1 1 1c0 1.25.2 2.45.57 3.57a1 1 0 0 1-.25 1z"/></svg>
          000 000 0000
        </li>
        <li class="contact-item">
          <svg viewBox="0 0 24 24" aria-hidden="true"><path d="M2 5h20v2.2l-10 6.3L2 7.2z M2 9.5l10 6.3 10-6.3V19H2z"/></svg>
          youremail@vardena.example
        </li>
      </ul>
    </div>
  </section>

  <section class="card card--back">
    <div class="brand-square"></div>
    <p class="brand-large">Vardena General Painting Ltd.</p>
  </section>
</main>
</body>
</html>
```